Design a web site for my business - Brellan Coatworks Mackaby.

We are a family business that handles design, fabrication and installation of powder coated aluminum, stainless steel and glass products. Including handrails, privacy slat screens, electric gates and pool fencing. We are based in the Whitsundays in North Queensland and service an area from Airlie Beach to Townsville.

Target Market(s)

Domestic and commercial

Industry/Entity Type

fabrication - manufacturing

Coding

Coded - Design and coding required

Number of Pages Required

5+ page

Colors
0054AA
0677BA
7BADD7
CADEEF
E8F1F8

Requirements
Must have
• photo galleries, contact page, one page for privacy screens, balustrades, glass fencing, stainless steel handrail, powder coated aluminium handrails and pool fencing

```html
<!DOCTYPE html>
<html lang="en">
<head>
<meta charset="utf-8">
<title>Brellan Coatworks Mackaby</title>
<link href="https://fonts.googleapis.com/css2?family=Montserrat:wght@600;700&family=Nunito+Sans:wght@400;600;700&display=swap" rel="stylesheet">
<style>
:root{
  --blue:#0677ba;
  --blue-deep:#0054aa;
  --blue-soft:#7badd7;
  --ink:#1f1f1f;
  --text:#444;
  --muted:#777;
  --dark:#2d2d2d;
  --about-bg:#e6e6e6;
  --light-bg:#f8f8f8;
  --btn-grey:#c9ccd1;
  --white:#fff;
}
*{margin:0;padding:0;box-sizing:border-box}
html,body{width:1200px;height:4041px;overflow:hidden}
body{position:relative;font-family:"Nunito Sans",sans-serif;color:var(--text);background:var(--white)}
.abs{position:absolute}
h1,h2,h3{font-family:"Montserrat",sans-serif;font-weight:700}

/* header */
.site-header{left:0;top:0;width:1200px;height:65px;background:var(--white)}
.brand{left:66px;top:8px;font-family:"Montserrat",sans-serif;font-weight:700;font-size:21px;line-height:25px;color:var(--ink)}
.topbar{right:66px;top:8px;display:flex;gap:36px;font-size:13px;color:var(--ink);align-items:center}
.topbar span{display:flex;align-items:center;gap:10px}
.nav{top:40px;left:543px;display:flex;font-size:13px;color:#555}
.nav a{text-decoration:none;color:inherit;margin-right:79px}
.nav a:last-child{margin-right:0}
.nav .active{color:var(--blue)}

/* hero */
.hero{left:0;top:65px;width:1200px;height:563px;background:linear-gradient(180deg,#8a9aa5 0%,#4d6b5a 30%,#3d5147 45%,#2a6f93 62%,#1d5c82 80%,#cfd3d4 100%)}
.hero::after{content:"";position:absolute;inset:0;background:linear-gradient(90deg,rgba(0,0,0,.35),rgba(0,0,0,.05))}
.hero-title{left:66px;top:182px;font-size:48px;line-height:61px;color:var(--white);z-index:2}
.hero-title .accent{color:var(--blue)}
.hero-sub{left:66px;top:389px;width:560px;font-size:18px;line-height:25px;color:var(--white);z-index:2}
.btn{display:inline-flex;align-items:center;justify-content:center;gap:8px;border-radius:5px;font-size:13px;text-transform:uppercase;text-decoration:none}
.btn-primary{background:var(--blue);color:var(--white)}
.hero-btn{left:66px;top:471px;width:137px;height:41px;z-index:2}
.hero-dots{left:22px;top:326px;z-index:2;display:flex;flex-direction:column;gap:5px}
.hero-dots i{width:11px;height:11px;border-radius:50%;background:#dcdcdc}
.hero-dots i:first-child{background:var(--blue)}

/* section heading */
.section-title{left:0;width:1200px;text-align:center;font-size:46px;color:var(--ink)}
.rule{left:514px;width:172px;height:2px;background:var(--ink)}
.rule.short{left:558px;width:85px}

/* services */
.services{left:0;top:628px;width:1200px;height:1055px;background:var(--dark)}
.services .section-title{color:var(--white)}
.services .rule{background:var(--white)}
.service-grid{left:69px;top:875px;display:grid;grid-template-columns:repeat(3,333px);gap:32px 31px}
.service-card{height:345px;border:2px solid #9a9a9a;border-radius:10px;background:linear-gradient(180deg,#5a5a5a,#3b3b3b);padding:14px}
.service-inner{height:100%;background:var(--white);border-radius:8px;padding:28px 22px 0 22px}
.service-icon{width:66px;height:66px;stroke:#111;fill:none;stroke-width:2}
.service-inner h3{font-size:24px;line-height:31px;color:var(--ink);margin-top:26px;text-transform:uppercase}
.service-inner p{font-size:13.5px;line-height:22px;color:var(--text);margin-top:12px}
.btn-ghost{background:var(--btn-grey);color:#3d6d9a;height:34px;padding:0 18px;margin-top:16px;font-weight:600}

/* about */
.about{left:0;top:1683px;width:1200px;height:627px;background:var(--about-bg)}
.about-bar{left:69px;top:1836px;width:10px;height:322px;background:var(--blue)}
.about-photo{left:79px;top:1766px;width:512px;height:461px;background:linear-gradient(135deg,#1d3a52 0%,#30506b 45%,#6b7c84 70%,#1f3346 100%)}
.about-title{left:650px;top:1765px;font-size:40px;color:var(--ink)}
.about-text{left:650px;top:1836px;width:490px;font-size:15px;line-height:28px;color:var(--muted)}
.feature{display:flex;align-items:center;gap:16px;font-size:19px;line-height:28px;color:#444}
.feature .dot{width:47px;height:47px;border-radius:50%;background:var(--white);display:flex;align-items:center;justify-content:center;flex:none}
.feature svg{width:26px;height:26px;stroke:var(--blue);fill:none;stroke-width:2}
.about-btn{left:650px;top:2202px;width:136px;height:37px}

/* values */
.values{left:0;top:2310px;width:1200px;height:1368px;background:var(--light-bg)}
.value-card{width:340px}
.value-photo{height:230px;border-radius:10px;box-shadow:0 3px 8px rgba(0,0,0,.25)}
.value-card p{text-align:center;font-size:19px;line-height:28px;color:#333;margin-top:20px;font-weight:600}

/* service area */
.area-text{left:270px;top:3053px;width:660px;text-align:center;font-size:15px;line-height:23px;color:#333}
.map{left:66px;top:3132px;width:1068px;height:455px;border-radius:12px;background:linear-gradient(110deg,#d6eedd 0%,#bfe6cf 35%,#a8dcc8 55%,#93d4e6 75%,#8fd0ea 100%);box-shadow:0 3px 8px rgba(0,0,0,.2)}

/* footer */
.footer{left:0;top:3678px;width:1200px;height:363px;background:var(--dark);color:var(--white)}
.footer-brand{left:152px;top:3780px;font-family:"Montserrat",sans-serif;font-weight:700;font-size:38px;line-height:46px;color:var(--blue)}
.footer-col h4{font-size:12px;font-weight:700;padding-bottom:6px;border-bottom:2px solid var(--blue);display:inline-block}
.footer-col ul{list-style:none;margin-top:22px;font-size:12px;line-height:36px}
.contact-list{list-style:none;margin-top:22px;font-size:12px}
.contact-list li{display:flex;gap:14px;align-items:flex-start;margin-bottom:16px;line-height:15px}
.contact-list .ico{width:24px;height:24px;border-radius:50%;background:#444;flex:none;display:flex;align-items:center;justify-content:center}
.contact-list svg{width:12px;height:12px;fill:var(--blue)}
.subscribe{display:flex;margin-top:20px;width:236px;height:33px;border-radius:17px;overflow:hidden;background:var(--white)}
.subscribe span{flex:1;color:#333;font-size:12px;display:flex;align-items:center;padding-left:16px;gap:10px}
.subscribe b{width:62px;background:var(--blue);display:flex;align-items:center;justify-content:center}
.socials{left:66px;top:3992px;display:flex;gap:7px}
.socials i{width:31px;height:31px;border-radius:50%;border:2px solid var(--white)}
.socials i:first-child{background:var(--blue);border-color:var(--blue)}
.copyright{left:0;width:1200px;top:4002px;text-align:center;font-size:12px;font-weight:700}
</style>
</head>
<body>

<header class="abs site-header">
  <div class="abs brand">Logo<br>Here</div>
  <div class="abs topbar">
    <span><svg width="12" height="16" viewBox="0 0 12 16" fill="none" stroke="#0677ba" stroke-width="1.6"><rect x="1.5" y="1" width="9" height="14" rx="1.5"/></svg>+123456789</span>
    <span><svg width="16" height="16" viewBox="0 0 16 16" fill="none" stroke="#0677ba" stroke-width="1.4"><path d="M1 7 15 1 10 15 7.5 9z"/><path d="M7.5 9 15 1"/></svg>info@sitename.com</span>
  </div>
  <nav class="abs nav">
    <a class="active" href="#">Home</a><a href="#">About</a><a href="#">Services</a><a href="#">Gallery</a><a href="#">Product</a><a href="#">Contact</a>
  </nav>
</header>

<section class="abs hero" role="img" aria-label="Photo of a backyard pool with aluminium pool fencing and palm trees"></section>
<h1 class="abs hero-title">CUSTOM ALUMINUM<br>STEEL &amp; GLASS<br><span class="accent">FABRICATORS</span></h1>
<p class="abs hero-sub">Premium Handrails, Pool Fencing &amp; Gates From Airlie Beach To Townsville. Family-Owned &amp; Built For NQ.</p>
<a class="abs btn btn-primary hero-btn" href="#">Contact Us</a>
<div class="abs hero-dots"><i></i><i></i><i></i></div>

<section class="abs services"></section>
<h2 class="abs section-title" style="top:703px;color:#fff">OUR SERVICES</h2>
<div class="abs rule" style="top:795px;background:#fff"></div>
<div class="abs rule short" style="top:806px;background:#fff"></div>

<div class="abs service-grid">
  <article class="service-card"><div class="service-inner">
    <svg class="service-icon" viewBox="0 0 66 66"><path d="M2 62h12v-12h12v-12h12v-12h12v-12h12"/><path d="M2 46 50 4M8 62V42M20 50V32M32 38V22M44 26V12"/></svg>
    <h3>Handrails</h3>
    <p>Lorem ipsum dolor sit amet, consectetur adipiscing elit. Maecenas fermentum, nisi sit amet lobortis congue</p>
    <a class="btn btn-ghost" href="#">Learn More ›</a>
  </div></article>
  <article class="service-card"><div class="service-inner">
    <svg class="service-icon" viewBox="0 0 66 66"><rect x="2" y="2" width="62" height="62"/><path d="M14 64V14h38v50M22 64V22h22v42M30 22v42M36 22v42"/><rect x="54" y="30" width="6" height="10"/></svg>
    <h3 style="margin-top:34px">Electric Gates</h3>
    <p>Lorem ipsum dolor sit amet, consectetur adipiscing elit. Maecenas fermentum, nisi sit amet lobortis congue</p>
    <a class="btn btn-ghost" href="#">Learn More ›</a>
  </div></article>
  <article class="service-card"><div class="service-inner">
    <svg class="service-icon" viewBox="0 0 66 66"><path d="M2 64V14l7-8 7 8v50M16 64V14l8-8 8 8v50M32 64V14l8-8 8 8v50M48 64V14l8-8 8 8v50M2 64h62"/><circle cx="9" cy="28" r="1"/><circle cx="24" cy="28" r="1"/><circle cx="40" cy="28" r="1"/><circle cx="56" cy="28" r="1"/></svg>
    <h3>Pool Fencing</h3>
    <p>Lorem ipsum dolor sit amet, consectetur adipiscing elit. Maecenas fermentum, nisi sit amet lobortis congue</p>
    <a class="btn btn-ghost" href="#">Learn More ›</a>
  </div></article>
  <article class="service-card"><div class="service-inner">
    <svg class="service-icon" viewBox="0 0 66 66"><rect x="4" y="2" width="58" height="8"/><path d="M8 10v46h50V10M8 18h50M8 26h50M8 34h50M8 42h50M8 50h50M33 50v12"/></svg>
    <h3>Privacy Screens</h3>
    <p>Lorem ipsum dolor sit amet, consectetur adipiscing elit. Maecenas fermentum, nisi sit amet lobortis congue</p>
    <a class="btn btn-ghost" href="#">Learn More ›</a>
  </div></article>
  <article class="service-card"><div class="service-inner">
    <svg class="service-icon" viewBox="0 0 66 66"><path d="M6 2h46v62H6z"/><path d="M14 58l6-10M36 16l8-8M48 44l-6 6"/><path d="M16 12l2 5 5 2-5 2-2 5-2-5-5-2 5-2z"/><path d="M54 44l2 5 5 2-5 2-2 5-2-5-5-2 5-2z"/></svg>
    <h3>Glass<br>Installations</h3>
    <p>Lorem ipsum dolor sit amet, consectetur adipiscing elit. Maecenas fermentum, nisi</p>
    <a class="btn btn-ghost" href="#">Learn More ›</a>
  </div></article>
  <article class="service-card"><div class="service-inner">
    <svg class="service-icon" viewBox="0 0 66 66"><rect x="4" y="2" width="30" height="46"/><path d="M10 10h8v7h-8zM10 22h8v7h-8zM10 34h8v7h-8zM22 12h8M22 24h8M22 36h8"/><path d="M34 42l12-14 6 4-10 16-6 14-4-2z"/><path d="M56 24l4-4M58 30h6M56 36l4 4"/></svg>
    <h3>Custom<br>Fabrication</h3>
    <p>Lorem ipsum dolor sit amet, consectetur adipiscing elit. Maecenas fermentum, nisi</p>
    <a class="btn btn-ghost" href="#">Learn More ›</a>
  </div></article>
</div>

<section class="abs about"></section>
<div class="abs about-bar"></div>
<div class="abs about-photo" role="img" aria-label="Photo of a fabricator grinding metal with sparks flying"></div>
<h2 class="abs about-title">ABOUT</h2>
<p class="abs about-text">Lorem ipsum dolor sit amet, consectetur adipiscing elit. Praesent ut rhoncus lacus, vel tincidunt dolor. In sed ligula a turpis pharetra interdum. In vel felis aliquam, ultrices lacus ac, eleifend massa. Lorem ipsum dolor sit amet, consectetur adipiscing elit. Praesent ut rhoncus lacus, vel tincidunt dolor. In sed ligula a turpis pharetra interdum. In vel felis aliquam, ultrices lacus ac, eleifend massa.</p>
<div class="abs feature" style="left:650px;top:2037px"><span class="dot"><svg viewBox="0 0 26 26"><circle cx="13" cy="8" r="3"/><circle cx="5" cy="11" r="2.5"/><circle cx="21" cy="11" r="2.5"/><path d="M7 22c0-5 12-5 12 0M1 20c0-3 6-4 7-3M25 20c0-3-6-4-7-3"/></svg></span>Family Owned</div>
<div class="abs feature" style="left:891px;top:2037px"><span class="dot"><svg viewBox="0 0 26 26"><ellipse cx="13" cy="8" rx="10" ry="4"/><path d="M3 8v10c0 2 4 4 10 4s10-2 10-4V8M3 13c0 2 4 4 10 4s10-2 10-4"/></svg></span>Premium Materials</div>
<div class="abs feature" style="left:650px;top:2114px"><span class="dot"><svg viewBox="0 0 26 26"><circle cx="13" cy="8" r="4"/><path d="M9 6h8M4 24c0-7 4-9 9-9s9 2 9 9z"/></svg></span>Experienced<br>Fabricators</div>
<div class="abs feature" style="left:891px;top:2114px"><span class="dot"><svg viewBox="0 0 26 26"><path d="M20 14v8H4V6h8"/><path d="M11 15l1-4 9-9 3 3-9 9z"/></svg></span>Custom Solutions</div>
<a class="abs btn btn-primary about-btn" href="#">Learn More ›</a>

<section class="abs values"></section>
<h2 class="abs section-title" style="top:2383px">VALUE PROPOSITIONS</h2>
<div class="abs rule" style="top:2474px"></div>
<div class="abs rule short" style="top:2488px"></div>

<div class="abs value-card" style="left:69px;top:2540px">
  <div class="value-photo" role="img" aria-label="Photo of a powder coated aluminium profile on a workbench" style="background:linear-gradient(135deg,#6e6a66,#2e2c2b 60%,#4d4a47)"></div>
  <p>Cyclone-Rated Engineering &amp; Durable Powder Coating</p>
</div>
<div class="abs value-card" style="left:432px;top:2540px">
  <div class="value-photo" role="img" aria-label="Photo of a welder assembling a metal gate panel in the workshop" style="background:linear-gradient(135deg,#8a7a66,#4b4139 55%,#9a9088)"></div>
  <p>Full Service: Design, Fabrication &amp; Installation</p>
</div>
<div class="abs value-card" style="left:795px;top:2540px">
  <div class="value-photo" role="img" aria-label="Photo of the family business owners standing together outdoors" style="background:linear-gradient(135deg,#4f6b44,#7c8d6a 50%,#5d7491)"></div>
  <p>Local Family Business with Decades of Experience</p>
</div>

<h2 class="abs section-title" style="top:2915px">SERVICE AREA</h2>
<div class="abs rule" style="top:3005px"></div>
<div class="abs rule short" style="top:3019px"></div>
<p class="abs area-text">We are based in the Whitsundays in North Queensland and service an area from Airlie Beach to Townsville.</p>
<div class="abs map" role="img" aria-label="Map of the Whitsundays service area around Airlie Beach"></div>

<footer class="abs footer"></footer>
<div class="abs footer-brand">Logo<br>Here</div>
<div class="abs footer-col" style="left:337px;top:3728px">
  <h4>Quick Links</h4>
  <ul><li>Home</li><li>About</li><li>Services</li><li>Gallery</li><li>Product</li></ul>
</div>
<div class="abs footer-col" style="left:607px;top:3728px">
  <h4>Contact Us</h4>
  <ul class="contact-list">
    <li><span class="ico"><svg viewBox="0 0 12 12"><path d="M2 1l2.5 0 1 3-1.5 1a7 7 0 0 0 3 3l1-1.5 3 1V10c0 1-1 1.5-2 1.5A9 9 0 0 1 .5 3C.5 2 1 1 2 1z"/></svg></span><span style="padding-top:5px">+123456789</span></li>
    <li><span class="ico"><svg viewBox="0 0 12 12"><rect x="1" y="2.5" width="10" height="7" rx="1"/></svg></span><span style="padding-top:5px">info@companyname.com</span></li>
    <li><span class="ico"><svg viewBox="0 0 12 12"><path d="M6 .5a4 4 0 0 1 4 4c0 3-4 7-4 7s-4-4-4-7a4 4 0 0 1 4-4z"/></svg></span><span>18 Coral Way, North<br>Queensland</span></li>
  </ul>
</div>
<div class="abs footer-col" style="left:876px;top:3728px">
  <h4 style="border:0">Subscribe</h4>
  <div class="subscribe"><span><svg width="11" height="9" viewBox="0 0 11 9"><rect width="11" height="9" rx="1" fill="#333"/></svg>Email Address</span><b><svg width="14" height="14" viewBox="0 0 16 16" fill="none" stroke="#fff" stroke-width="1.5"><path d="M1 7 15 1 10 15 7.5 9z"/><path d="M7.5 9 15 1"/></svg></b></div>
</div>
<div class="abs socials"><i></i><i></i><i></i><i></i></div>
<p class="abs copyright">Copyright ©2026 sie name. All rights reserved.</p>

</body>
</html>
```